Biography Landing Page for Reid Falmor

We need a landing page design for the CEO of Brightfield Tandem (see BrightfieldTandem.com). We have a domains -
ReidFalmor.com
TheKeenestRancherOfTheHills.com
ReidFalmor.net
JnReidFalmor.com
JnReidFalmor.net

I will attached a color pallet for you to use. z

I am attaching the lengthy copy for the website. I look forward to seeing how you design this page. I recommend that there be options to expand / open copy for each of the major sections so the reader can see the headings and choose to open them to read more. But, be sure that the expanded sections are also designed.

I have a collection of photos to use for the site. We will slide those photos in later. For now, please leave lots of “for position only” spots for photos.

We will have lots of pictures to put on this site, but we will have those inserted later. For the design, please just use these few photos as placeholder

We will need all files in Figma Design (Desktop, Laptop, Mobile)

```html
<!DOCTYPE html>
<html lang="en">
<head>
<meta charset="utf-8">
<title>Reid Falmor — Biography</title>
<link href="https://fonts.googleapis.com/css2?family=Cinzel:wght@500;600;700&family=Cormorant+Garamond:wght@500;600&family=Inter:wght@400;500;600;700&display=swap" rel="stylesheet">
<style>
:root{
  --mat:#b3b3b3;
  --navy:#08131f;
  --navy-2:#0b1724;
  --card:#101c2a;
  --card-line:#1d2b3b;
  --gold:#b89968;
  --gold-light:#c9ab78;
  --gold-dark:#94754a;
  --red:#780909;
  --red-btn:#7d0b0b;
  --blue:#4a8fbc;
  --blue-dark:#0e2c45;
  --ink:#f3eee4;
  --muted:#a9b1bb;
}
*{box-sizing:border-box;margin:0;padding:0}
html,body{width:1200px;height:4360px;overflow:hidden;background:var(--mat)}
body{font-family:"Inter",sans-serif;color:var(--ink);position:relative}
.page{position:absolute;left:86px;top:85px;width:1027px;height:4187px;background:var(--navy);overflow:hidden}
.abs{position:absolute}
.eyebrow{font-size:13px;letter-spacing:2px;color:var(--gold);text-transform:uppercase;display:flex;align-items:center;justify-content:center;gap:10px}
.eyebrow::before,.eyebrow::after{content:"";width:50px;height:1px;background:var(--gold);opacity:.6}
.eyebrow.left{justify-content:flex-start}
.eyebrow.left::before{display:none}
.center{left:0;right:0;text-align:center}
.section-title{font-family:"Cinzel",serif;font-weight:600;font-size:34px;line-height:44px;color:#fff}
.section-sub{font-size:12px;color:#d5d9de}
.btn{display:inline-flex;align-items:center;justify-content:center;height:28px;padding:0 14px;border-radius:14px;font-size:13px;font-weight:700;white-space:nowrap}
.btn-gold{background:var(--gold);color:#1a1208}
.btn-red{background:var(--red-btn);color:#fff}
.btn-white{background:#fff;color:#111}
.btn-outline{border:1.5px solid #fff;color:#fff}
.btn-row{display:flex;gap:8px;justify-content:center}

/* hero */
.hero{left:0;top:0;width:1027px;height:720px;background:linear-gradient(100deg,#0d2a40 0%,#1d5679 40%,#3f86b3 75%,#4b92c0 100%)}
.hero-band{left:0;top:470px;width:1027px;height:250px;background:linear-gradient(172deg,rgba(8,19,31,.2) 0%,#2a2a2c 28%,#6e5a3d 48%,#5a1518 70%,#08131f 100%)}
.logo-box{left:61px;top:0;width:159px;height:115px;background:#fff;display:flex;align-items:center;justify-content:center;box-shadow:0 4px 12px rgba(0,0,0,.3)}
.logo-name{font-family:"Cinzel",serif;font-weight:600;font-size:19px;color:#1a2230}
.nav{right:18px;top:11px;display:flex;align-items:center;gap:22px;font-size:10px;color:#fff}
.nav-pill{border:1.5px solid var(--gold);border-radius:12px;padding:4px 9px;font-weight:700;font-size:9.5px}
.hero-eyebrow{left:61px;top:160px;font-size:13px;letter-spacing:1.5px;color:var(--gold-light)}
.hero-eyebrow::after{content:"";display:inline-block;width:34px;height:1px;background:var(--gold-light);margin-left:6px;vertical-align:middle}
.hero-title{left:61px;top:180px;width:520px;font-family:"Cinzel",serif;font-weight:600;font-size:37px;line-height:43px;color:var(--gold-light)}
.hero-copy{left:61px;top:315px;font-size:13px;line-height:20px;color:#fff}
.hero-btns{left:61px;top:368px;justify-content:flex-start}
.hero-quote{left:61px;top:410px;font-family:"Cinzel",serif;font-size:11.5px;font-weight:600;color:#fff}
.hero-art{left:489px;top:108px;width:480px;height:400px;border-radius:16px;background:linear-gradient(135deg,#2f6f98 0%,#1d4a68 45%,#8a7a4a 80%,#b8923e 100%);opacity:.85}

/* snapshot */
.snap-grid{left:100px;top:888px;width:829px;display:grid;grid-template-columns:repeat(3,1fr);gap:12px}
.snap-card{height:57px;background:var(--card);border:1px solid var(--card-line);border-radius:8px;padding:13px 14px}
.snap-label{font-size:7.5px;letter-spacing:1px;color:var(--gold);font-weight:600}
.snap-value{font-size:11px;font-weight:700;margin-top:5px}

/* gold panels */
.panel-gold{background:linear-gradient(120deg,#a88b5d 0%,#c2a676 50%,#9f8256 100%);border-radius:18px}
.panel-gold .eyebrow{color:#1c150c}
.panel-gold .eyebrow::before,.panel-gold .eyebrow::after{background:#1c150c}
.defiance{left:103px;top:1091px;width:821px;height:293px}
.panel-title{font-family:"Cinzel",serif;font-weight:600;color:#fff;font-size:35px;line-height:43px}
.panel-copy{font-size:11px;line-height:19px;color:#fff}

/* timeline */
.timeline{left:99px;top:1582px;width:829px;display:flex;flex-direction:column;gap:9px}
.tl-item{height:75px;background:var(--card);border:1px solid var(--card-line);border-radius:8px;position:relative;padding:14px 0 0 75px}
.tl-dot{position:absolute;left:16px;top:20px;width:34px;height:34px;border-radius:50%;background:var(--gold);color:#1b140a;font-family:"Cinzel",serif;font-size:13px;font-weight:700;display:flex;align-items:center;justify-content:center}
.tl-line{left:133px;top:1620px;width:2px;height:258px;background:var(--gold)}
.tl-title{font-family:"Cormorant Garamond",serif;font-size:19px;font-weight:600}
.tl-copy{font-size:10.5px;color:#d2d6db;margin-top:6px}

.stats{left:99px;top:1964px;width:829px;display:grid;grid-template-columns:repeat(4,1fr);gap:12px}
.stat{height:73px;background:var(--card);border:1px solid var(--card-line);border-radius:8px;text-align:center;padding-top:17px}
.stat-num{font-family:"Cormorant Garamond",serif;font-size:21px;font-weight:600;color:var(--gold-light)}
.stat-label{font-size:8px;color:#c8cdd3;margin-top:2px}

/* career */
.career{left:99px;top:2260px;width:829px;display:grid;grid-template-columns:repeat(3,1fr);gap:12px}
.career-card{height:151px;background:var(--card);border:1px solid var(--card-line);border-radius:8px;padding:18px 15px}
.career-num{font-family:"Cormorant Garamond",serif;font-size:19px;color:var(--gold-light)}
.career-title{font-family:"Cormorant Garamond",serif;font-size:18px;font-weight:600;margin-top:14px}
.career-copy{font-size:10px;line-height:18px;color:#d2d6db;margin-top:6px}

/* philosophy */
.philosophy{left:103px;top:2470px;width:821px;height:280px;background:var(--red);border-radius:18px}
.philosophy .eyebrow{color:var(--gold-light)}
.philosophy .eyebrow::before,.philosophy .eyebrow::after{background:var(--gold-light)}
.philo-quote{font-family:"Cinzel",serif;font-weight:600;font-size:27px;line-height:36px;color:var(--gold-light)}

/* photos */
.photo{background:radial-gradient(ellipse at 50% 0%,#1e2b3a 0%,#0f1a27 60%,#0c1622 100%);border:1px solid var(--card-line);border-radius:10px;display:flex;align-items:center;justify-content:center;font-size:8.5px;letter-spacing:1px;color:#8b95a1}

/* values */
.values-band{left:0;top:3359px;width:1027px;height:370px;background:var(--navy-2)}
.values-title{left:94px;top:3455px;font-family:"Cinzel",serif;font-weight:600;font-size:36px;line-height:42px;color:#fff}
.values-copy{left:94px;top:3590px;width:370px;font-size:12px;line-height:19px;color:#fff}
.values-grid{left:496px;top:3418px;width:427px;display:grid;grid-template-columns:1fr 1fr;gap:10px}
.value-card{height:92px;background:#111d2b;border:1px solid var(--card-line);border-radius:8px;padding:14px 15px}
.value-card.tall{height:112px}
.value-title{font-family:"Cormorant Garamond",serif;font-size:18px;font-weight:600}
.value-copy{font-size:9.5px;line-height:17px;color:#d2d6db;margin-top:6px}

/* cta */
.cta{left:103px;top:3757px;width:821px;height:259px}
.cta .btn{font-size:12px}

.footer-mark{left:0;right:0;top:4044px;display:flex;align-items:center;justify-content:center;gap:12px}
.footer-circle{width:72px;height:72px;border-radius:50%;border:2px solid var(--gold)}
.footer-name{font-family:"Cinzel",serif;font-weight:600;font-size:24px;color:var(--gold-light)}
.footer-note{top:4152px;font-size:10px;color:#fff}
</style>
</head>
<body>
<div class="page">

  <header class="abs hero">
    <div class="abs hero-art" role="img" aria-label="Illustration: two businessmen with a large magnifying glass over a glowing light bulb"></div>
    <div class="abs hero-band" role="img" aria-label="Decorative sweeping gold and red ribbon band with a star"></div>
    <div class="abs logo-box"><span class="logo-name">Reid Falmor</span></div>
    <nav class="abs nav">
      <span>Home</span><span>About</span><span>Story</span><span>Career</span><span>Brightfield Tandem</span>
      <span class="nav-pill">JOIN THE MOVEMENT</span>
    </nav>
    <p class="abs hero-eyebrow">BIOGRAPHY LANDING PAGE CONCEPT</p>
    <h1 class="abs hero-title">I Didn’t Just Learn From Failure — I Built My Empire From It</h1>
    <p class="abs hero-copy">Every setback became fuel. Every “no” became momentum.<br>I am not successful despite the struggle — I am built from it.</p>
    <div class="abs btn-row hero-btns"><span class="btn btn-gold">READ MY STORY</span><span class="btn btn-red">Explore Brightfield Tandem</span></div>
    <p class="abs hero-quote">“Every ‘no’ became the combustion for a bigger ‘yes’.”</p>
  </header>

  <p class="abs center eyebrow" style="top:755px">Quick Profile</p>
  <h2 class="abs center section-title" style="top:788px">The Executive Snapshot</h2>
  <p class="abs center section-sub" style="top:830px">A clean summary area you can keep as-is or edit later once the client finalizes all details and photography.</p>
  <div class="abs snap-grid">
    <div class="snap-card"><div class="snap-label">FULL NAME</div><div class="snap-value">Jonathan Reid Falmor</div></div>
    <div class="snap-card"><div class="snap-label">KNOWN AS</div><div class="snap-value">Reid</div></div>
    <div class="snap-card"><div class="snap-label">BIRTHPLACE</div><div class="snap-value">Indianapolis, Indiana</div></div>
    <div class="snap-card"><div class="snap-label">CURRENT RESIDENCE</div><div class="snap-value">Austin, Texas</div></div>
    <div class="snap-card"><div class="snap-label">PROFESSION</div><div class="snap-value">CEO, Speaker, Investor, Podcaster</div></div>
    <div class="snap-card"><div class="snap-label">ORGANIZATION</div><div class="snap-value">Brightfield Tandem</div></div>
  </div>

  <section class="abs panel-gold defiance">
    <p class="abs center eyebrow" style="top:46px">Quick Profile</p>
    <h2 class="abs center panel-title" style="top:66px">A Life Defined by Defiance,<br>Leadership, and Reinvention</h2>
    <p class="abs center panel-copy" style="top:164px">From early adversity to national business leadership, Reid Falmor built a career by transforming setbacks into scale.<br>His story spans entrepreneurship, healthcare, finance, advocacy, and the creation of Brightfield Tandem.</p>
    <div class="abs center btn-row" style="top:218px"><span class="btn btn-white">READ MY STORY</span><span class="btn btn-red">Explore Brightfield Tandem</span></div>
  </section>

  <p class="abs center eyebrow" style="top:1447px">Life Journey</p>
  <h2 class="abs center section-title" style="top:1470px">From Early Adversity to<br>National Influence</h2>
  <div class="abs tl-line"></div>
  <div class="abs timeline">
    <div class="tl-item"><span class="tl-dot">01</span><div class="tl-title">Early Life</div><div class="tl-copy">Born into difficult circumstances, Falmor’s earliest years were shaped by hardship, resilience, and a refusal to be defined by limitation.</div></div>
    <div class="tl-item"><span class="tl-dot">02</span><div class="tl-title">Defying the Odds</div><div class="tl-copy">A life-threatening childhood accident became part of a larger story of perseverance, grit, and survival.</div></div>
    <div class="tl-item"><span class="tl-dot">03</span><div class="tl-title">Identity and Restoration</div><div class="tl-copy">After decades of living with an imposed identity, he reclaimed his original name and reasserted his personal truth.</div></div>
    <div class="tl-item"><span class="tl-dot">04</span><div class="tl-title">Business Growth</div><div class="tl-copy">From personal trainer to executive leader, Falmor built and scaled multiple businesses across fitness, finance, and healthcare.</div></div>
  </div>
  <div class="abs stats">
    <div class="stat"><div class="stat-num">12+</div><div class="stat-label">Major Facilities Built</div></div>
    <div class="stat"><div class="stat-num">1M+</div><div class="stat-label">Square Feet Operated</div></div>
    <div class="stat"><div class="stat-num">1000+</div><div class="stat-label">Sales Team Recruited</div></div>
    <div class="stat"><div class="stat-num">Nationwide</div><div class="stat-label">Leadership &amp; Impact</div></div>
  </div>

  <p class="abs center eyebrow" style="top:2116px">Career Highlights</p>
  <h2 class="abs center section-title" style="top:2140px">Leadership, Scale, and<br>Strategic Vision</h2>
  <div class="abs career">
    <div class="career-card"><div class="career-num">01</div><div class="career-title">Leadership at Scale</div><div class="career-copy">Built high-growth organizations, led national teams, and scaled operations across multiple industries.</div></div>
    <div class="career-card"><div class="career-num">02</div><div class="career-title">Brightfield Tandem</div><div class="career-copy">A platform centered on transparency, accountability, and empowering the Office of the Citizen.</div></div>
    <div class="career-card"><div class="career-num">03</div><div class="career-title">Patriotic Identity</div><div class="career-copy">A personal brand rooted in faith, resilience, conviction, and a strong sense of national purpose.</div></div>
  </div>

  <section class="abs philosophy">
    <p class="abs center eyebrow" style="top:48px">Core Philosophy</p>
    <p class="abs center philo-quote" style="top:74px">The credit belongs to the man who is<br>actually in the arena — the one who strives,<br>fails, dares greatly, and rises again.</p>
    <div class="abs center btn-row" style="top:200px"><span class="btn btn-white">READ MY STORY</span><span class="btn btn-outline">Explore Brightfield Tandem</span></div>
  </section>

  <p class="abs center eyebrow" style="top:2811px">Photo Layout</p>
  <h2 class="abs center section-title" style="top:2835px">Image Placeholder Section</h2>
  <p class="abs center section-sub" style="top:2886px">This area gives you premium blocks for future biography photos, campaign-style images, and featured moments.</p>
  <div class="abs photo" style="left:96px;top:2932px;width:300px;height:334px" role="img" aria-label="Featured biography photo">FEATURED IMAGE PLACEHOLDER</div>
  <div class="abs photo" style="left:411px;top:2932px;width:250px;height:160px" role="img" aria-label="Biography photo">PHOTO PLACEHOLDER</div>
  <div class="abs photo" style="left:675px;top:2932px;width:251px;height:160px" role="img" aria-label="Biography photo">PHOTO PLACEHOLDER</div>
  <div class="abs photo" style="left:411px;top:3106px;width:515px;height:160px" role="img" aria-label="Wide biography photo">WIDE PHOTO PLACEHOLDER</div>

  <div class="abs values-band"></div>
  <p class="abs eyebrow left" style="left:94px;top:3424px">Core Values</p>
  <h2 class="abs values-title">Faith, Family,<br>Resilience, and<br>Responsibility</h2>
  <p class="abs values-copy">Built on a belief in service, conviction, and personal responsibility, this personal brand narrative is designed to feel strong, polished, and deeply mission-driven.</p>
  <div class="abs values-grid">
    <div class="value-card"><div class="value-title">Faith</div><div class="value-copy">Grounded in spiritual conviction and Biblical principles.</div></div>
    <div class="value-card"><div class="value-title">Family</div><div class="value-copy">Driven by loyalty, caregiving, and personal devotion.</div></div>
    <div class="value-card tall"><div class="value-title">Resilience</div><div class="value-copy">A life story shaped by endurance, restoration, and forward motion.</div></div>
    <div class="value-card tall"><div class="value-title">Patriotism</div><div class="value-copy">A strong identity tied to citizenship, accountability, and the American spirit.</div></div>
  </div>

  <section class="abs panel-gold cta">
    <p class="abs center eyebrow" style="top:46px">Call to Action</p>
    <h2 class="abs center panel-title" style="top:70px">Join the Movement</h2>
    <p class="abs center" style="top:118px;font-size:15px;line-height:23px;color:#fff">Use this section for final call-to-action, social links, a lead<br>capture form, or direct traffic to Brightfield Tandem.</p>
    <div class="abs center btn-row" style="top:190px"><span class="btn btn-white">LEARN MORE</span><span class="btn btn-red">FOLLOW THE STORY</span></div>
  </section>

  <div class="abs footer-mark"><span class="footer-circle"></span><span class="footer-name">Reid Falmor</span></div>
  <p class="abs center footer-note">Premium biography landing page concept with editable placeholders and expanded sections.</p>
</div>
</body>
</html>
```